Makeup By Lorna

I am a makeup artist looking for professional looking double sided business card. I would like to create a logo and incorporate a set of eyes as the periods above the name "Lorna" on the card.

front of card: Logo "Beauty by Lorna" written across diagonal (bottom left to top right)

Back of card:
1) Professional makeup artist serving New York & New Jersey (or similar to this text)
2) 917-555-0148
3) beautybylorna@mailhaven.example

```html
<!DOCTYPE html>
<html lang="en">
<head>
<meta charset="utf-8">
<title>Beauty by Lorna – Business Card</title>
<link rel="stylesheet" href="https://fonts.googleapis.com/css2?family=Comfortaa:wght@300;500&family=Oswald:wght@300;400&display=swap">
<style>
  :root {
    --page-bg: #ffffff;
    --plum: #4e1f33;
    --plum-ink: #561e35;
    --mist: #dde6e5;
    --mist-edge: #c9d5d4;
    --card-text: #e6ecea;
  }
  * { margin: 0; padding: 0; box-sizing: border-box; }
  html, body {
    width: 1200px;
    height: 1000px;
    overflow: hidden;
    background: var(--page-bg);
  }
  .canvas {
    width: 1200px;
    height: 1000px;
    display: flex;
    flex-direction: column;
    align-items: center;
    justify-content: center;
    gap: 60px;
  }
  .card {
    width: 665px;
    height: 380px;
    position: relative;
    overflow: hidden;
  }
  .card--contact {
    background: var(--plum);
    color: var(--card-text);
    padding: 52px 56px;
  }
  .contact__title {
    font-family: "Comfortaa", sans-serif;
    font-weight: 500;
    font-size: 52px;
    letter-spacing: 1px;
    line-height: 1.1;
    margin-bottom: 26px;
  }
  .contact__tagline {
    font-family: "Oswald", sans-serif;
    font-weight: 400;
    font-size: 23px;
    line-height: 1.25;
    letter-spacing: 0.5px;
    margin-bottom: 30px;
  }
  .contact__line {
    font-family: "Oswald", sans-serif;
    font-weight: 300;
    font-size: 23px;
    letter-spacing: 0.8px;
    margin-bottom: 22px;
  }
  .contact__line--phone { font-weight: 400; }
  .card--brand {
    background: linear-gradient(160deg, var(--mist) 0%, #e8eeed 50%, var(--mist-edge) 100%);
    display: flex;
    align-items: center;
    justify-content: center;
    gap: 22px;
  }
  .brand__dot {
    width: 22px;
    height: 22px;
    border-radius: 50%;
    background: var(--plum-ink);
  }
  .brand__name {
    font-family: "Comfortaa", sans-serif;
    font-weight: 300;
    font-size: 120px;
    letter-spacing: 14px;
    color: var(--plum-ink);
  }
</style>
</head>
<body>
  <main class="canvas">
    <section class="card card--contact" aria-label="Business card, contact side">
      <h1 class="contact__title">Beauty by Lorna</h1>
      <p class="contact__tagline">Professional makeup artist serving<br>New York &amp; New Jersey</p>
      <p class="contact__line contact__line--phone">917-555-0148</p>
      <p class="contact__line contact__line--email">beautybylorna@mailhaven.example</p>
    </section>
    <section class="card card--brand" aria-label="Business card, brand side">
      <span class="brand__dot" aria-hidden="true"></span>
      <span class="brand__name">Lorna</span>
    </section>
  </main>
</body>
</html>
```